Wine label for new boutique South African wine focused on the USA market.

Wine label required for new ethical south African red wine called PLUMB which stands for 'Marlowe, tolland, brightly and you' but is also a play on 'SA' and that it has a story to tell. Gerald Marlowe is the wine maker, Tolland the farm owner, and Brightly an investor.

Concept is a simple old type writer font on a white/off white label. Front label would say 'Plumb No.1, 2010 Shiraz, South Africa' and similarly a second for another wine 'Plumb No.2, 2010 Cab/Merlot Blend. Maybe the round stain of the bottom of a wine bottle in the bottom corner? Would also like for the 'plumb' to double up as the logo and work in the form of a stamp.

The rear label will need to tell a short story and be able to accommodate the usual boilerplate info. The story will go something like, ' Plumb No.1: It's a long story, but in short we love our wine and we think you will too. The cooling see breezes of the Indian Ocean help define this world class Shiraz from the Western Cape. Aged in french oak for 20 months, the bold flavors will compliment all red meats or simply enjoy on its own. Learn more about our story at www.plumbvintners.example.

The cab/merlot will read similar: Plumb No.2: It's a long story, but in short we love our wine and we think you will too. The cooling see breezes of the Indian Ocean help define this world class red blend from the Western Cape. Aged in french oak for 20 months, this wine will compliment all red meats or simply enjoy on its own. Learn more about our story at www.plumbvintners.example.

Reason: Had some great designs already, but as i get to understand how ArtBazaarly works, I'm keen to explore as many ideas as possible. Neil

Thanks for all the great designs everybody!

We will make a tough decision in the next couple of days.

Regards

Neil

Target Market(s)

Middle class with some wine knowledge. Price point around $20 -30

Industry/Entity Type

Boutique

Requirements
Nice to have
• A small nod to the wine coming from south Africa in the design would be nice but nothing to over the top
Should not have
• Simple and clear font with plenty of empty space on the label

```html
<!DOCTYPE html>
<html lang="en">
<head>
<meta charset="utf-8">
<title>Plumb Wine Labels</title>
<link href="https://fonts.googleapis.com/css2?family=Cinzel:wght@400&display=swap" rel="stylesheet">
<style>
  :root {
    --bg: #ffffff;
    --label-black: #141414;
    --motif-green: #2f8a3c;
    --motif-yellow: #f6d41d;
    --flag-red: #d8322a;
    --flag-blue: #1f2a8f;
    --gold: #f2c81c;
    --ink-light: #e9e6dc;
  }
  * { margin: 0; padding: 0; box-sizing: border-box; }
  html, body {
    width: 888px;
    height: 1200px;
    overflow: hidden;
    background: var(--bg);
  }
  .label-set {
    width: 888px;
    height: 1200px;
    display: flex;
    justify-content: center;
    align-items: center;
    gap: 36px;
  }
  .wine-label {
    position: relative;
    width: 390px;
    height: 518px;
    background: var(--label-black);
    font-family: "Cinzel", "Times New Roman", serif;
    font-weight: 400;
    text-align: center;
    overflow: hidden;
  }
  .motif {
    position: absolute;
    background: linear-gradient(180deg, var(--motif-green) 0%, var(--motif-green) 60%, var(--motif-yellow) 100%);
  }
  .motif--top {
    top: 0;
    left: 57px;
    width: 276px;
    height: 98px;
  }
  .motif--bottom {
    bottom: 0;
    left: 126px;
    width: 138px;
    height: 72px;
    background: linear-gradient(0deg, var(--motif-green) 0%, var(--motif-green) 60%, var(--motif-yellow) 100%);
  }
  .edge-stripe {
    position: absolute;
    top: 312px;
    width: 10px;
    height: 38px;
  }
  .edge-stripe--red { left: 0; background: var(--flag-red); }
  .edge-stripe--blue { right: 0; background: var(--flag-blue); }
  .varietal {
    position: absolute;
    left: 0;
    right: 0;
    top: 160px;
    color: var(--ink-light);
    font-size: 20px;
    line-height: 20px;
  }
  .varietal small {
    display: block;
    font-size: 9px;
    line-height: 14px;
    letter-spacing: 0.4px;
    margin-top: 1px;
  }
  .brand {
    position: absolute;
    left: 0;
    right: 0;
    top: 306px;
    color: var(--gold);
    font-size: 44px;
    font-weight: 400;
    line-height: 48px;
    letter-spacing: 1px;
  }
  .edition {
    position: absolute;
    left: 0;
    right: 0;
    top: 364px;
    color: var(--gold);
    font-size: 26px;
    line-height: 30px;
  }
  .vintage {
    position: absolute;
    left: 0;
    right: 0;
    top: 412px;
    color: var(--gold);
    font-size: 22px;
    line-height: 26px;
  }
</style>
</head>
<body>
<main class="label-set">

  <section class="wine-label">
    <div class="motif motif--top" role="img" aria-label="Green and yellow chevron motif nodding to South Africa"></div>
    <span class="edge-stripe edge-stripe--red"></span>
    <span class="edge-stripe edge-stripe--blue"></span>
    <p class="varietal">Shiraz<small>South Africa</small></p>
    <h2 class="brand">PLUMB</h2>
    <p class="edition">No. 1</p>
    <p class="vintage">2010</p>
    <div class="motif motif--bottom" role="img" aria-label="Small green and yellow chevron motif"></div>
  </section>

  <section class="wine-label">
    <div class="motif motif--top" role="img" aria-label="Green and yellow chevron motif nodding to South Africa"></div>
    <span class="edge-stripe edge-stripe--red"></span>
    <span class="edge-stripe edge-stripe--blue"></span>
    <p class="varietal">Cab/Merlot<br>Blend<small>South Africa</small></p>
    <h2 class="brand">PLUMB</h2>
    <p class="edition">No. 2</p>
    <p class="vintage">2010</p>
    <div class="motif motif--bottom" role="img" aria-label="Small green and yellow chevron motif"></div>
  </section>

</main>
</body>
</html>
```